Business Card Design Project

Hello! We need a business card design for a new company opening up in Downtown Dallas called Marbury Cupcakes. We are a cupcake factory and our primary colors are Tiffany Blue and Brown. We want to have a design that can be used for multiple positions (Owner/Operations Manager, Assistant Operations Manager, Decorator, Baker, Corporate Sale Rep, Special Events Rep etc) We would like for it to be double sided. Use the following information in your designs:

Renata Vankirk
Assistant Operations Manager
renata@marburycupcakes.example
T555.318.4907

Store Hours:
Mon-Thur 10am-9pm
Fri-Sat 10am-10pm
Sun 12pm-7pm

website: www.marburycupcakes.example

Address: 2735 Birch Ave, Dallas TX 70519

The logo is attached.

Industry/Entity Type

Business

Requirements
Must have
• It must be Tiffany Blue and Brown.
Nice to have
• Nice for it to be double sided.
Should not have
• No graphics like a cupcake. Just the word logo.

```html
<!DOCTYPE html>
<html lang="en">
<head>
<meta charset="utf-8">
<title>Marbury Cupcakes — Business Card</title>
<link rel="stylesheet" href="https://fonts.googleapis.com/css2?family=Josefin+Slab:wght@400;600&family=Josefin+Sans:wght@400&display=swap">
<style>
  :root {
    --tiffany: #5bbcc2;
    --brown: #4a2a22;
    --brown-soft: #5a3a30;
    --paper: #fbfbfb;
    --backdrop: #e6eaea;
    --rule: #b89a90;
  }
  * { box-sizing: border-box; margin: 0; padding: 0; }
  html, body { width: 1200px; height: 900px; overflow: hidden; }
  body {
    background: var(--backdrop);
    font-family: "Josefin Slab", Georgia, serif;
    color: var(--brown);
    position: relative;
  }
  .card {
    position: absolute;
    left: 270px;
    width: 660px;
    height: 378px;
    background: var(--paper);
    overflow: hidden;
    box-shadow: 0 6px 18px rgba(0,0,0,0.12);
  }
  .card--front { top: 54px; }
  .card--back { top: 468px; }
  .card__wave { position: absolute; inset: 0; width: 100%; height: 100%; }
  .wordmark {
    position: absolute;
    font-family: "Josefin Slab", Georgia, serif;
    font-weight: 600;
    color: var(--tiffany);
    white-space: nowrap;
    letter-spacing: 0.5px;
  }
  .card--front .wordmark { left: 40px; top: 48px; font-size: 34px; }
  .card--back .wordmark { right: 44px; top: 100px; font-size: 50px; }
  .identity { position: absolute; right: 40px; top: 96px; text-align: right; }
  .identity__name { font-size: 34px; color: var(--tiffany); letter-spacing: 2px; font-weight: 400; line-height: 40px; }
  .identity__title { font-family: "Josefin Sans", Arial, sans-serif; font-size: 15px; color: var(--brown); margin-top: 2px; }
  .identity__rule { position: absolute; right: 40px; top: 168px; width: 290px; height: 1px;
    background: linear-gradient(to right, transparent, var(--rule)); }
  .contact { position: absolute; right: 40px; top: 180px; list-style: none; text-align: right; }
  .contact li { font-size: 16px; letter-spacing: 1px; line-height: 26px; color: var(--brown); white-space: nowrap; }
  .contact svg { width: 11px; height: 11px; margin-left: 8px; vertical-align: 0; fill: var(--tiffany); }
  .website { position: absolute; left: 72px; bottom: 22px; font-size: 15px; letter-spacing: 1.5px; color: var(--brown-soft); white-space: nowrap; }
  .hours { position: absolute; left: 90px; bottom: 26px; font-size: 16px; letter-spacing: 1.5px; line-height: 22px; color: var(--brown-soft); white-space: nowrap; }
  .hours__label { text-transform: uppercase; }
</style>
</head>
<body>

<section class="card card--front" aria-label="Card front">
  <svg class="card__wave" viewBox="0 0 660 378" preserveAspectRatio="none" aria-hidden="true">
    <path d="M0 378 C 50 330, 110 300, 210 298 C 330 296, 420 330, 520 318 C 590 308, 630 300, 660 288 L 660 378 Z" fill="var(--tiffany)"/>
    <path d="M0 378 C 50 330, 110 300, 210 298 C 330 296, 420 330, 520 318 C 590 308, 630 300, 660 288" fill="none" stroke="var(--brown)" stroke-width="1.6"/>
  </svg>
  <div class="wordmark">Marbury Cupcakes</div>
  <div class="identity">
    <h1 class="identity__name">Renata Vankirk</h1>
    <p class="identity__title">Assistant Operations Manager</p>
  </div>
  <div class="identity__rule"></div>
  <ul class="contact">
    <li>2735 Birch Ave, Dallas TX 70519<svg viewBox="0 0 12 12"><path d="M6 1 L11 6 H9.5 V11 H7 V8 H5 V11 H2.5 V6 H1 Z"/></svg></li>
    <li>555.318.4907<svg viewBox="0 0 12 12"><path d="M2.5 1 L4.5 1 L5.5 3.8 L4.2 4.8 C5 6.5 5.8 7.3 7.3 8 L8.2 6.6 L11 7.6 V9.6 C11 10.4 10.4 11 9.6 11 C5 11 1 7 1 2.4 C1 1.6 1.6 1 2.5 1 Z"/></svg></li>
    <li>renata@marburycupcakes.example<svg viewBox="0 0 12 12"><path d="M1 2.5 H11 V9.5 H1 Z M1.8 3.2 L6 6.4 L10.2 3.2" fill="none" stroke="var(--tiffany)" stroke-width="1.1"/></svg></li>
  </ul>
  <p class="website">www.marburycupcakes.example</p>
</section>

<section class="card card--back" aria-label="Card back">
  <svg class="card__wave" viewBox="0 0 660 378" preserveAspectRatio="none" aria-hidden="true">
    <path d="M0 378 C 30 300, 90 250, 200 245 C 320 240, 420 250, 520 235 C 590 225, 630 210, 660 200 L 660 378 Z" fill="var(--tiffany)"/>
    <path d="M0 378 C 30 300, 90 250, 200 245 C 320 240, 420 250, 520 235 C 590 225, 630 210, 660 200" fill="none" stroke="var(--brown)" stroke-width="1.6"/>
  </svg>
  <div class="wordmark">Marbury Cupcakes</div>
  <div class="hours">
    <p class="hours__label">Store Hours:</p>
    <p>Mon-Thur 10am-9pm • Sun 12pm-7pm</p>
    <p>Fri-Sat 10am-10pm</p>
  </div>
</section>

</body>
</html>
```